Pop Up Banner Design (30x72in) for events for Meridian Tongue Institute

30 x 72 inch design for a pop up banner or 2 (or 3) to advertise my business, Meridian Tongue Institute, featuring www.meridiantongueinst.com

This banner will be used at anime conventions, or local events to promote the business to the general public, schools, or asian culture lovers.

Color scheme to identify with the logo that is attached. Imagery would be great!

Target audience: teens to 30s
Benefits MTI Offers: learning japanese language, learning japanese culture, peer study groups and events, one-on-one or classroom setting, in person or virtual learning, Standard Lexical Aptitude Exam (SLAE) preparation, homework, guided tours to Japan once a year, translation services, conversation tables, etc.

Target Market(s)

teens to 30 year olds

Industry/Entity Type

Education

Font styles to use
Sans Serif

Colors
ec1f27
ffffff
000000

Requirements
Must have
• logo, imagery, benefits strategically explained, website

```html
<!DOCTYPE html>
<html lang="en">
<head>
<meta charset="utf-8">
<title>Meridian Tongue Institute – Pop Up Banner</title>
<link rel="stylesheet" href="https://fonts.googleapis.com/css2?family=Arimo:wght@700&family=Roboto+Condensed:wght@300;400&display=swap">
<style>
  :root {
    --brand-red: #c8262e;
    --maroon: #7d2a2b;
    --white: #ffffff;
    --ink: #1a1a1a;
    --orange: #f08a1c;
    --yellow: #ffd21a;
    --footer-ink: #2a1a2e;
  }
  * { margin: 0; padding: 0; box-sizing: border-box; }
  html, body { width: 1200px; height: 2878px; overflow: hidden; background: var(--white); }
  .banner { position: relative; width: 1200px; height: 2878px; background: var(--white); overflow: hidden; }

  .brand { position: absolute; top: 0; left: 0; width: 1200px; height: 640px; }
  .brand-mark { position: absolute; left: 404px; top: 112px; width: 410px; height: 410px; border-radius: 50%; background: var(--brand-red); }
  .brand-name {
    position: absolute; top: 535px; left: 0; width: 1200px; text-align: center;
    font-family: "Roboto Condensed", sans-serif; font-weight: 300; font-size: 74px;
    line-height: 90px; color: var(--ink); letter-spacing: 0.5px;
  }

  .hero { position: absolute; top: 620px; left: 0; width: 1200px; height: 1420px; display: block; }

  .info { position: absolute; top: 1940px; left: 0; width: 1200px; height: 938px; background: var(--maroon); }
  .section-head {
    position: absolute; left: 0; width: 1200px; background: var(--white);
    font-family: "Arimo", sans-serif; font-weight: 700; color: var(--ink);
    padding-left: 78px; display: flex; align-items: center; white-space: nowrap;
  }
  .benefits-head { top: 91px; height: 70px; font-size: 50px; }
  .exam-head { top: 523px; height: 71px; font-size: 48px; padding-left: 68px; }
  .list {
    position: absolute; left: 78px; list-style: none; white-space: nowrap;
    font-family: "Roboto Condensed", sans-serif; font-weight: 400; font-size: 52px;
    line-height: 63px; color: var(--white);
  }
  .list li::before { content: "•"; margin-right: 14px; }
  .benefits-list { top: 170px; }
  .exam-list { top: 606px; }
  .exam-list .sep::before { content: "•"; margin: 0 14px; }

  .footer {
    position: absolute; left: 0; top: 2788px; width: 1200px; height: 90px;
    background: linear-gradient(90deg, var(--orange) 0%, var(--yellow) 50%, var(--orange) 100%);
    display: flex; align-items: center; justify-content: center;
    font-family: "Arimo", sans-serif; font-weight: 700; font-size: 37px; color: var(--footer-ink);
  }
</style>
</head>
<body>
<div class="banner">
  <header class="brand">
    <div class="brand-mark"></div>
    <h1 class="brand-name">MERIDIAN TONGUE INSTITUTE</h1>
  </header>

  <svg class="hero" viewBox="0 0 1200 1420" xmlns="http://www.w3.org/2000/svg">
    <defs>
      <linearGradient id="swoosh" x1="0" y1="0" x2="1" y2="0">
        <stop offset="0" stop-color="#f7a21b"/>
        <stop offset="0.5" stop-color="#ef6a1d"/>
        <stop offset="1" stop-color="#d9262b"/>
      </linearGradient>
      <linearGradient id="swooshLow" x1="0" y1="0" x2="1" y2="0">
        <stop offset="0" stop-color="#e0312a"/>
        <stop offset="0.5" stop-color="#f07a1c"/>
        <stop offset="1" stop-color="#ffc21a"/>
      </linearGradient>
      <radialGradient id="photoTone" cx="0.5" cy="0.52" r="0.62">
        <stop offset="0" stop-color="#2e2a2e"/>
        <stop offset="0.35" stop-color="#4a3c3c"/>
        <stop offset="0.6" stop-color="#b58c78"/>
        <stop offset="0.8" stop-color="#8c96a0"/>
        <stop offset="1" stop-color="#7b8792"/>
      </radialGradient>
    </defs>
    <rect x="0" y="1000" width="1200" height="420" fill="var(--maroon)"/>
    <path d="M0,360 Q520,60 1200,95 L1200,1090 Q700,1275 0,1272 Z" fill="url(#photoTone)" role="img" aria-label="Photo of a smiling group of young students in a huddle, looking up at the camera"/>
    <path d="M0,300 Q500,-10 1200,30 L1200,95 Q520,60 0,362 Z" fill="url(#swoosh)"/>
    <path d="M0,282 Q500,-28 1200,12 L1200,30 Q500,-10 0,300 Z" fill="var(--yellow)" opacity="0.85"/>
    <path d="M0,1270 Q700,1275 1200,1072 L1200,1210 Q700,1360 0,1360 Z" fill="url(#swooshLow)"/>
    <path d="M0,1360 Q700,1360 1200,1210 L1200,1420 L0,1420 Z" fill="var(--maroon)"/>
  </svg>

  <section class="info">
    <h2 class="section-head benefits-head">Benefits MTI Offers:</h2>
    <ul class="list benefits-list">
      <li>Learning Japanese Language</li>
      <li>Learning Japanese Culture</li>
      <li>Peer Study Groups And Events</li>
      <li>One-on-one Or Classroom Setting</li>
      <li>In Person Or Virtual Learning</li>
    </ul>
    <h2 class="section-head exam-head">Standard Lexical Aptitude Exam (SLAE)</h2>
    <ul class="list exam-list">
      <li>Preparation<span class="sep"></span>Homework</li>
      <li>Guided tours to Japan once a year</li>
      <li>Translation Services<span class="sep"></span>Conversation Tables, etc.</li>
    </ul>
  </section>

  <footer class="footer">For more information visit at www.meridiantongueinst.com</footer>
</div>
</body>
</html>
```